Audio Spectrum Infographic

We need an infographic similar to the attached for an online course. There are a few changes but we are generally looking for better colors and a less cluttered design with more clarity.

For the types (Vocals -Harp) we would like to include as many as possible without the clutter. Better fonts and non-distracting background colors will help.

The Sound Effects section (Rumble, Tinny, etc) needs to stay but perhaps more buttons and less lines. We would like it to be easy to read and less cluttered.

The "UQA 1/3rd octave Equalizer Bands" and wave image can be removed.

The Sub Bass, Bass, Midrange, High Mids, High Frequency information needs to stay.

We will have other graphics to complete once this is completed.

```html
<!DOCTYPE html>
<html lang="en">
<head>
<meta charset="utf-8">
<title>Audio Frequency Spectrum</title>
<link rel="stylesheet" href="https://fonts.googleapis.com/css2?family=Roboto+Condensed:wght@400;700&display=swap">
<style>
  :root {
    --page: #ffffff;
    --frame: #231f20;
    --zone-sub: #3d3b3c;
    --zone-bass: #6a6869;
    --zone-mid: #8a8889;
    --zone-himid: #a09e9f;
    --zone-high: #b6b4b5;
    --grid: rgba(255,255,255,0.16);
    --divider: rgba(255,255,255,0.28);
    --fundamental: #b9321c;
    --harmonic: #f6e35a;
    --overtone: #1c1a1a;
    --label: #ffffff;
    --keyboard-light: #f0f0f0;
    --keyboard-mid: #d4d4d4;
    --pill-a: #c63b1f;
    --pill-b: #6e1a0c;
  }
  html, body {
    margin: 0;
    width: 1200px;
    height: 783px;
    overflow: hidden;
    background: var(--page);
  }
  .spectrum-chart { display: block; font-family: "Roboto Condensed", "Arial Narrow", sans-serif; }
  .axis-label { fill: var(--label); font-size: 11px; text-anchor: middle; }
  .scale-label { fill: var(--label); font-size: 11px; font-weight: 700; text-anchor: middle; }
  .region-label { fill: var(--label); font-size: 13px; font-weight: 700; text-anchor: middle; }
  .family-label { fill: var(--label); font-size: 13px; font-weight: 700; text-anchor: middle; }
  .instrument-label { fill: var(--label); font-size: 11px; font-weight: 700; text-anchor: end; }
  .instrument-label.after { text-anchor: start; }
  .grid-line { stroke: var(--grid); stroke-width: 1; }
  .section-divider { stroke: var(--divider); stroke-width: 1; stroke-dasharray: 5 4; }
  .band-rule { stroke: #ffffff; stroke-width: 1.5; }
  .range { stroke-width: 5; stroke-linecap: round; fill: none; }
  .range.fundamental { stroke: var(--fundamental); }
  .range.harmonic { stroke: var(--harmonic); }
  .range.overtone-edge { stroke: var(--harmonic); stroke-width: 6; }
  .range.overtone { stroke: var(--overtone); stroke-width: 3.5; }
  .range.low-limit { stroke: #ffffff; }
  .piano-title { fill: var(--label); font-size: 13px; font-weight: 700; text-anchor: middle; }
  .piano-bracket { stroke: var(--fundamental); stroke-width: 1; fill: none; }
  .marker-line { stroke: var(--fundamental); stroke-width: 1.5; }
  .marker-label { fill: var(--label); font-size: 11px; text-anchor: middle; }
  .effect-pill rect { fill: url(#pillFill); filter: url(#pillShadow); }
  .effect-pill text { fill: var(--label); font-size: 11px; text-anchor: middle; dominant-baseline: central; }
  .effect-pill.small text { font-size: 8px; font-weight: 700; }
</style>
</head>
<body>
<svg class="spectrum-chart" width="1200" height="783" viewBox="0 0 1300 848" role="img" aria-label="Audio frequency spectrum chart of instrument ranges and tonal descriptors">
  <defs>
    <linearGradient id="pillFill" x1="0" y1="0" x2="1" y2="0">
      <stop offset="0" stop-color="var(--pill-a)"/>
      <stop offset="1" stop-color="var(--pill-b)"/>
    </linearGradient>
    <linearGradient id="keyboardFill" x1="0" y1="0" x2="0" y2="1">
      <stop offset="0" stop-color="var(--keyboard-light)"/>
      <stop offset="1" stop-color="var(--keyboard-mid)"/>
    </linearGradient>
    <filter id="pillShadow" x="-10%" y="-30%" width="120%" height="180%">
      <feDropShadow dx="1" dy="2" stdDeviation="1.2" flood-color="#000" flood-opacity="0.45"/>
    </filter>
    <filter id="panelShadow" x="-5%" y="-5%" width="110%" height="110%">
      <feDropShadow dx="0" dy="2" stdDeviation="4" flood-color="#000" flood-opacity="0.3"/>
    </filter>
  </defs>

  <!-- panel -->
  <g filter="url(#panelShadow)">
    <rect x="153" y="38" width="992" height="779" fill="var(--frame)"/>
  </g>

  <!-- frequency zones -->
  <g class="zones">
    <rect x="189" y="68" width="180" height="695" fill="var(--zone-sub)"/>
    <rect x="369" y="68" width="184" height="695" fill="var(--zone-bass)"/>
    <rect x="553" y="68" width="275" height="695" fill="var(--zone-mid)"/>
    <rect x="828" y="68" width="142" height="695" fill="var(--zone-himid)"/>
    <rect x="970" y="68" width="175" height="695" fill="var(--zone-high)"/>
    <rect x="189" y="763" width="180" height="27" fill="var(--zone-sub)"/>
    <rect x="369" y="763" width="184" height="27" fill="var(--zone-bass)"/>
    <rect x="553" y="763" width="275" height="27" fill="var(--zone-mid)"/>
    <rect x="828" y="763" width="142" height="27" fill="var(--zone-himid)"/>
    <rect x="970" y="763" width="175" height="27" fill="var(--zone-high)"/>
  </g>

  <!-- grid -->
  <g class="grid">
    <line class="grid-line" x1="218" y1="68" x2="218" y2="738"/><line class="grid-line" x1="250" y1="68" x2="250" y2="738"/>
    <line class="grid-line" x1="278" y1="68" x2="278" y2="738"/><line class="grid-line" x1="317" y1="68" x2="317" y2="738"/>
    <line class="grid-line" x1="346" y1="68" x2="346" y2="738"/><line class="grid-line" x1="389" y1="68" x2="389" y2="738"/>
    <line class="grid-line" x1="410" y1="68" x2="410" y2="738"/><line class="grid-line" x1="435" y1="68" x2="435" y2="738"/>
    <line class="grid-line" x1="466" y1="68" x2="466" y2="738"/><line class="grid-line" x1="491" y1="68" x2="491" y2="738"/>
    <line class="grid-line" x1="518" y1="68" x2="518" y2="738"/><line class="grid-line" x1="550" y1="68" x2="550" y2="738"/>
    <line class="grid-line" x1="577" y1="68" x2="577" y2="738"/><line class="grid-line" x1="617" y1="68" x2="617" y2="738"/>
    <line class="grid-line" x1="645" y1="68" x2="645" y2="738"/><line class="grid-line" x1="678" y1="68" x2="678" y2="738"/>
    <line class="grid-line" x1="710" y1="68" x2="710" y2="738"/><line class="grid-line" x1="736" y1="68" x2="736" y2="738"/>
    <line class="grid-line" x1="767" y1="68" x2="767" y2="738"/><line class="grid-line" x1="799" y1="68" x2="799" y2="738"/>
    <line class="grid-line" x1="828" y1="68" x2="828" y2="738"/><line class="grid-line" x1="857" y1="68" x2="857" y2="738"/>
    <line class="grid-line" x1="887" y1="68" x2="887" y2="738"/><line class="grid-line" x1="915" y1="68" x2="915" y2="738"/>
    <line class="grid-line" x1="945" y1="68" x2="945" y2="738"/><line class="grid-line" x1="979" y1="68" x2="979" y2="738"/>
    <line class="grid-line" x1="1005" y1="68" x2="1005" y2="738"/><line class="grid-line" x1="1038" y1="68" x2="1038" y2="738"/>
    <line class="grid-line" x1="1066" y1="68" x2="1066" y2="738"/><line class="grid-line" x1="1096" y1="68" x2="1096" y2="738"/>
    <line class="grid-line" x1="1124" y1="68" x2="1124" y2="738"/>
  </g>

  <!-- section dividers -->
  <g>
    <line class="section-divider" x1="153" y1="112" x2="1145" y2="112"/>
    <line class="section-divider" x1="153" y1="214" x2="1145" y2="214"/>
    <line class="section-divider" x1="153" y1="300" x2="1145" y2="300"/>
    <line class="section-divider" x1="153" y1="434" x2="1145" y2="434"/>
    <line class="section-divider" x1="153" y1="553" x2="1145" y2="553"/>
  </g>

  <!-- top axis -->
  <g class="top-axis">
    <text class="axis-label" x="172" y="57">Hz</text>
    <text class="axis-label" x="218" y="57">20</text><text class="axis-label" x="318" y="57">40</text>
    <text class="axis-label" x="364" y="57">60</text><text class="axis-label" x="435" y="57">100</text>
    <text class="axis-label" x="513" y="57">200</text><text class="axis-label" x="620" y="57">400</text>
    <text class="axis-label" x="670" y="57">600</text><text class="axis-label" x="739" y="57">1K</text>
    <text class="axis-label" x="831" y="57">2K</text><text class="axis-label" x="920" y="57">4K</text>
    <text class="axis-label" x="971" y="57">6K</text><text class="axis-label" x="1035" y="57">10K</text>
    <text class="axis-label" x="1093" y="57">16K</text><text class="axis-label" x="1127" y="57">20K</text>
  </g>

  <!-- family labels -->
  <g>
    <text class="family-label" transform="translate(176 90) rotate(90)">Vocal</text>
    <text class="family-label" transform="translate(176 163) rotate(90)">Percussion</text>
    <text class="family-label" transform="translate(176 258) rotate(90)">Brass</text>
    <text class="family-label" transform="translate(176 368) rotate(90)">Woodwinds</text>
    <text class="family-label" transform="translate(176 493) rotate(90)">Strings</text>
  </g>

  <!-- instrument ranges -->
  <g class="instrument-ranges">
    <line class="range harmonic" x1="724" y1="82" x2="1097" y2="82"/>
    <line class="range overtone-edge" x1="1013" y1="82" x2="1097" y2="82"/><line class="range overtone" x1="1013" y1="82" x2="1097" y2="82"/>
    <line class="range fundamental" x1="437" y1="82" x2="724" y2="82"/>
    <text class="instrument-label" x="431" y="86">Male</text>

    <line class="range harmonic" x1="742" y1="98" x2="1097" y2="98"/>
    <line class="range overtone-edge" x1="1013" y1="98" x2="1097" y2="98"/><line class="range overtone" x1="1013" y1="98" x2="1097" y2="98"/>
    <line class="range fundamental" x1="553" y1="98" x2="742" y2="98"/>
    <text class="instrument-label" x="544" y="102">Female</text>

    <line class="range harmonic" x1="643" y1="125" x2="1005" y2="125"/><line class="range fundamental" x1="346" y1="125" x2="643" y2="125"/>
    <text class="instrument-label" x="337" y="129">Kick</text>
    <line class="range harmonic" x1="684" y1="140" x2="880" y2="140"/><line class="range fundamental" x1="371" y1="140" x2="684" y2="140"/>
    <text class="instrument-label" x="362" y="144">Tympany</text>
    <line class="range harmonic" x1="643" y1="156" x2="994" y2="156"/><line class="range fundamental" x1="388" y1="156" x2="643" y2="156"/>
    <text class="instrument-label" x="378" y="160">Toms</text>
    <line class="range harmonic" x1="553" y1="171" x2="1035" y2="171"/><line class="range fundamental" x1="435" y1="171" x2="553" y2="171"/>
    <text class="instrument-label" x="426" y="175">Snare</text>
    <line class="range harmonic" x1="732" y1="186" x2="950" y2="186"/><line class="range fundamental" x1="488" y1="186" x2="732" y2="186"/>
    <text class="instrument-label" x="477" y="190">Congas</text>
    <line class="range harmonic" x1="723" y1="202" x2="1090" y2="202"/><line class="range fundamental" x1="580" y1="202" x2="723" y2="202"/>
    <line class="range overtone" x1="510" y1="202" x2="580" y2="202" style="stroke-width:5"/>
    <text class="instrument-label" x="498" y="206">Cymbals</text>

    <line class="range harmonic" x1="606" y1="228" x2="830" y2="228"/><line class="range fundamental" x1="328" y1="228" x2="606" y2="228"/>
    <line class="range low-limit" x1="277" y1="228" x2="328" y2="228"/>
    <text class="instrument-label" x="264" y="232">Tuba</text>
    <line class="range harmonic" x1="709" y1="243" x2="950" y2="243"/><line class="range fundamental" x1="388" y1="243" x2="709" y2="243"/>
    <line class="range overtone" x1="365" y1="243" x2="388" y2="243" style="stroke-width:5"/>
    <text class="instrument-label" x="351" y="247">French Horn</text>
    <line class="range harmonic" x1="617" y1="258" x2="1032" y2="258"/>
    <line class="range overtone-edge" x1="947" y1="258" x2="1032" y2="258"/><line class="range overtone" x1="947" y1="258" x2="1032" y2="258"/>
    <line class="range fundamental" x1="367" y1="258" x2="617" y2="258"/>
    <text class="instrument-label" x="352" y="262">Bass Trombone</text>
    <line class="range harmonic" x1="651" y1="273" x2="1038" y2="273"/>
    <line class="range overtone-edge" x1="954" y1="273" x2="1038" y2="273"/><line class="range overtone" x1="954" y1="273" x2="1038" y2="273"/>
    <line class="range fundamental" x1="412" y1="273" x2="651" y2="273"/>
    <text class="instrument-label" x="396" y="277">Tenor Trombone</text>
    <line class="range harmonic" x1="761" y1="289" x2="1027" y2="289"/><line class="range fundamental" x1="497" y1="289" x2="761" y2="289"/>
    <text class="instrument-label" x="481" y="293">Trumpet</text>

    <line class="range harmonic" x1="516" y1="315" x2="916" y2="315"/><line class="range fundamental" x1="256" y1="315" x2="516" y2="315"/>
    <text class="instrument-label after" x="938" y="319">Contrabassoon</text>
    <line class="range harmonic" x1="678" y1="330" x2="1024" y2="330"/><line class="range fundamental" x1="363" y1="330" x2="678" y2="330"/>
    <text class="instrument-label" x="347" y="334">Bassoon</text>
    <line class="range harmonic" x1="690" y1="346" x2="1077" y2="346"/>
    <line class="range overtone-edge" x1="1013" y1="346" x2="1077" y2="346"/><line class="range overtone" x1="1013" y1="346" x2="1077" y2="346"/>
    <line class="range fundamental" x1="455" y1="346" x2="690" y2="346"/>
    <text class="instrument-label" x="436" y="350">Tenor Sax</text>
    <line class="range harmonic" x1="698" y1="361" x2="1077" y2="361"/>
    <line class="range overtone-edge" x1="1013" y1="361" x2="1077" y2="361"/><line class="range overtone" x1="1013" y1="361" x2="1077" y2="361"/>
    <line class="range fundamental" x1="471" y1="361" x2="698" y2="361"/>
    <text class="instrument-label" x="456" y="365">Alto Sax</text>
    <line class="range harmonic" x1="834" y1="377" x2="1068" y2="377"/><line class="range fundamental" x1="471" y1="377" x2="834" y2="377"/>
    <text class="instrument-label" x="457" y="381">Clarinet</text>
    <line class="range harmonic" x1="802" y1="392" x2="1068" y2="392"/><line class="range fundamental" x1="541" y1="392" x2="802" y2="392"/>
    <text class="instrument-label" x="528" y="396">Oboe</text>
    <line class="range harmonic" x1="839" y1="407" x2="1056" y2="407"/><line class="range fundamental" x1="555" y1="407" x2="839" y2="407"/>
    <text class="instrument-label" x="543" y="411">Flute</text>
    <line class="range harmonic" x1="914" y1="423" x2="1073" y2="423"/><line class="range fundamental" x1="673" y1="423" x2="914" y2="423"/>
    <text class="instrument-label" x="657" y="427">Piccolo</text>

    <line class="range harmonic" x1="597" y1="448" x2="950" y2="448"/><line class="range fundamental" x1="316" y1="448" x2="597" y2="448"/>
    <line class="range overtone" x1="277" y1="448" x2="316" y2="448" style="stroke-width:5"/>
    <text class="instrument-label" x="261" y="452">Bass</text>
    <line class="range harmonic" x1="650" y1="464" x2="1000" y2="464"/><line class="range fundamental" x1="377" y1="464" x2="650" y2="464"/>
    <text class="instrument-label" x="365" y="468">Cello</text>
    <line class="range harmonic" x1="735" y1="479" x2="980" y2="479"/><line class="range fundamental" x1="466" y1="479" x2="735" y2="479"/>
    <text class="instrument-label" x="451" y="483">Viola</text>
    <line class="range harmonic" x1="771" y1="494" x2="1090" y2="494"/><line class="range fundamental" x1="523" y1="494" x2="771" y2="494"/>
    <text class="instrument-label" x="509" y="498">Violin</text>
    <line class="range harmonic" x1="759" y1="510" x2="948" y2="510"/><line class="range fundamental" x1="409" y1="510" x2="759" y2="510"/>
    <text class="instrument-label" x="397" y="514">Guitar</text>
    <line class="range harmonic" x1="887" y1="525" x2="968" y2="525"/><line class="range fundamental" x1="267" y1="525" x2="887" y2="525"/>
    <text class="instrument-label" x="253" y="529">Harp</text>
    <line class="range fundamental" x1="219" y1="540" x2="1002" y2="540"/>
    <text class="instrument-label after" x="1020" y="544">Pipe Organ</text>
  </g>

  <!-- piano -->
  <g class="piano">
    <polyline class="piano-bracket" points="252,587 252,572 513,572"/>
    <polyline class="piano-bracket" points="657,572 930,572 930,587"/>
    <text class="piano-title" x="585" y="576">Standard 88-key Piano</text>

    <rect class="keyboard-area" x="189" y="590" width="908" height="38" fill="url(#keyboardFill)" role="img" aria-label="88-key piano keyboard with octaves 0 to 9 laid along the frequency axis"/>

    <line class="marker-line" x1="561" y1="628" x2="561" y2="640"/>
    <text class="marker-label" x="562" y="656">Middle C</text>
    <line class="marker-line" x1="632" y1="628" x2="632" y2="640"/>
    <text class="marker-label" x="632" y="651">A</text>
    <text class="marker-label" x="632" y="665">440</text>
  </g>

  <!-- tonal descriptors -->
  <g class="effects">
    <g class="effect-pill"><rect x="258" y="640" width="54" height="16" rx="8"/><text x="285" y="648">Rumble</text></g>
    <g class="effect-pill"><rect x="216" y="666" width="84" height="17" rx="8.5"/><text x="258" y="674.5">Chest/Thump</text></g>
    <g class="effect-pill"><rect x="373" y="659" width="45" height="16" rx="8"/><text x="395.5" y="667">Bottom</text></g>
    <g class="effect-pill small"><rect x="343" y="686" width="45" height="16" rx="8"/><text x="365.5" y="694">AC/Ground</text></g>
    <g class="effect-pill"><rect x="475" y="675" width="68" height="17" rx="8.5"/><text x="509" y="683.5">Warmth</text></g>
    <g class="effect-pill"><rect x="434" y="703" width="70" height="17" rx="8.5"/><text x="469" y="711.5">Boom/Punch</text></g>
    <g class="effect-pill"><rect x="548" y="691" width="84" height="17" rx="8.5"/><text x="590" y="699.5">Fullness/Mud</text></g>
    <g class="effect-pill"><rect x="632" y="673" width="92" height="17" rx="8.5"/><text x="678" y="681.5">Honk</text></g>
    <g class="effect-pill"><rect x="703" y="647" width="98" height="17" rx="8.5"/><text x="752" y="655.5">Whack</text></g>
    <g class="effect-pill"><rect x="737" y="691" width="93" height="17" rx="8.5"/><text x="783.5" y="699.5">Tinny</text></g>
    <g class="effect-pill"><rect x="825" y="657" width="82" height="17" rx="8.5"/><text x="866" y="665.5">Crunch</text></g>
    <g class="effect-pill"><rect x="898" y="680" width="64" height="17" rx="8.5"/><text x="930" y="688.5">Edge</text></g>
    <g class="effect-pill"><rect x="919" y="635" width="110" height="17" rx="8.5"/><text x="974" y="643.5">Sibilance</text></g>
    <g class="effect-pill"><rect x="965" y="661" width="68" height="17" rx="8.5"/><text x="999" y="669.5">Definition</text></g>
    <g class="effect-pill"><rect x="1017" y="688" width="41" height="17" rx="8.5"/><text x="1037.5" y="696.5">Pierce</text></g>
    <g class="effect-pill"><rect x="1080" y="648" width="60" height="16" rx="8"/><text x="1110" y="656">Air</text></g>
    <g class="effect-pill"><rect x="829" y="715" width="298" height="17" rx="8.5"/><text x="978" y="723.5">Treble</text></g>
  </g>

  <!-- 1/3 octave scale -->
  <g class="third-octave">
    <text class="scale-label" x="218" y="752">20</text><text class="scale-label" x="250" y="752">25</text>
    <text class="scale-label" x="280" y="752">31.5</text><text class="scale-label" x="317" y="752">40</text>
    <text class="scale-label" x="346" y="752">50</text><text class="scale-label" x="389" y="752">63</text>
    <text class="scale-label" x="410" y="752">80</text><text class="scale-label" x="435" y="752">100</text>
    <text class="scale-label" x="466" y="752">125</text><text class="scale-label" x="491" y="752">160</text>
    <text class="scale-label" x="518" y="752">200</text><text class="scale-label" x="550" y="752">250</text>
    <text class="scale-label" x="577" y="752">315</text><text class="scale-label" x="617" y="752">400</text>
    <text class="scale-label" x="645" y="752">500</text><text class="scale-label" x="678" y="752">630</text>
    <text class="scale-label" x="710" y="752">800</text><text class="scale-label" x="736" y="752">1K</text>
    <text class="scale-label" x="767" y="752">1.25K</text><text class="scale-label" x="799" y="752">1.6K</text>
    <text class="scale-label" x="828" y="752">2K</text><text class="scale-label" x="857" y="752">2.5K</text>
    <text class="scale-label" x="887" y="752">3.15K</text><text class="scale-label" x="915" y="752">4K</text>
    <text class="scale-label" x="945" y="752">5K</text><text class="scale-label" x="979" y="752">6.3K</text>
    <text class="scale-label" x="1005" y="752">8K</text><text class="scale-label" x="1038" y="752">10K</text>
    <text class="scale-label" x="1066" y="752">12.5K</text><text class="scale-label" x="1096" y="752">16K</text>
    <text class="scale-label" x="1124" y="752">20K</text>
  </g>

  <!-- regions -->
  <line class="band-rule" x1="153" y1="763" x2="1145" y2="763"/>
  <line class="band-rule" x1="153" y1="790" x2="1145" y2="790"/>
  <g class="regions">
    <text class="region-label" x="280" y="781">Sub Bass</text>
    <text class="region-label" x="462" y="782">Bass</text>
    <text class="region-label" x="691" y="782">Mid Range</text>
    <text class="region-label" x="899" y="781">High Mids</text>
    <text class="region-label" x="1057" y="782">High Freqs</text>
  </g>

  <!-- bottom axis -->
  <g class="bottom-axis">
    <text class="axis-label" x="172" y="808">Hz</text>
    <text class="axis-label" x="218" y="808">20</text><text class="axis-label" x="318" y="808">40</text>
    <text class="axis-label" x="364" y="808">60</text><text class="axis-label" x="435" y="808">100</text>
    <text class="axis-label" x="513" y="808">200</text><text class="axis-label" x="620" y="808">400</text>
    <text class="axis-label" x="670" y="808">600</text><text class="axis-label" x="739" y="808">1K</text>
    <text class="axis-label" x="831" y="808">2K</text><text class="axis-label" x="920" y="808">4K</text>
    <text class="axis-label" x="971" y="808">6K</text><text class="axis-label" x="1035" y="808">10K</text>
    <text class="axis-label" x="1093" y="808">16K</text><text class="axis-label" x="1127" y="808">20K</text>
  </g>
</svg>
</body>
</html>
```